Studying Effectively To Do List

I am looking to design a new "Study To Do List" for High School students (Ages 15 - 18) . This will be printed as an A4 notepad and so should only be a single A4 page.

The Design will need to be professional and look semi-serious but also be appealing to High school students (Ages 15 - 18) and should NOT be gender specific.

I have attached a word document outlining the structure of the page. The space provided should be large enough that people can write in it comfortably.

The notepad will most likely be printed in black and white but I'm also looking at coloured options - colours should be kept to a minimum.

This will be printed professionally and should also include a 3mm bleed.

The design should also include the business logo (included in the word document)

Target Market(s)

High School students (Ages 15 - 18). Both genders

Industry/Entity Type

Education

Font styles to use
Serif
Sans Serif

Requirements
Must have
• Please see the word document attached.
Should not have
• Too much colour

```html
<!DOCTYPE html>
<html lang="en">
<head>
<meta charset="utf-8">
<title>Northpath – Study To Do List</title>
<link rel="stylesheet" href="https://fonts.googleapis.com/css2?family=Montserrat:wght@400;500;600;700&display=swap">
<style>
:root{
  --navy:#1f2b3e;
  --orange:#e85a1b;
  --ink:#2b3340;
  --rule:#9aa1ab;
  --paper:#ffffff;
  --backdrop:#e9e7e4;
  --faint:#e3e6ea;
}
*{box-sizing:border-box;margin:0;padding:0}
html,body{width:1200px;height:800px;overflow:hidden}
body{background:var(--backdrop);font-family:"Montserrat",Arial,sans-serif;color:var(--ink)}
.sheet{position:absolute;left:330px;top:18px;width:540px;height:764px;background:var(--paper);box-shadow:0 6px 24px rgba(0,0,0,.18);overflow:hidden}
.edge-band{position:absolute;left:0;top:0;width:26px;height:764px}
.faint-name{position:absolute;left:26px;right:0;top:380px;text-align:center;font-weight:700;font-size:44px;color:var(--faint);letter-spacing:1px;pointer-events:none}
.content{position:absolute;left:54px;right:34px;top:22px;bottom:16px;display:flex;flex-direction:column}
.masthead{display:flex;align-items:center;justify-content:space-between;height:44px}
.brand{display:flex;align-items:center;gap:8px;font-weight:700;font-size:20px;color:var(--navy);margin-left:120px}
.brand .dot{width:14px;height:14px;border-radius:50%;background:var(--orange)}
.date{font-size:9px;font-weight:500;display:flex;align-items:flex-end;gap:4px}
.date .fill{width:110px;border-bottom:1px solid var(--rule);height:10px}
.section-tag{display:inline-block;align-self:flex-start;background:var(--navy);color:#fff;font-size:8.5px;font-weight:600;letter-spacing:.8px;padding:2px 6px;margin:8px 0 2px}
.cols{display:grid;grid-template-columns:1fr 1fr;column-gap:0}
.cols .col+.col{border-left:1px solid var(--rule);padding-left:6px}
.row{display:flex;align-items:flex-end;height:17.5px;font-size:8.5px;gap:4px}
.row .label{white-space:nowrap}
.row .fill{flex:1;border-bottom:1px solid var(--rule);height:100%}
.row .due{white-space:nowrap}
.row .fill.short{flex:0 0 80px}
.divider{border-top:1px dashed var(--rule);margin-top:6px}
.boxes{display:grid;grid-template-columns:1fr 1fr;gap:10px;margin-top:10px}
.box{border:1px solid var(--navy);padding:2px 8px 4px;background:var(--paper)}
.box h3{font-size:9px;font-weight:600;text-align:center;letter-spacing:.8px;color:var(--navy);border-bottom:1px solid var(--navy);padding-bottom:2px}
.box .row{height:15px}
.url{margin-top:auto;text-align:right;font-size:10px;font-weight:700;letter-spacing:1.4px;color:var(--navy)}
</style>
</head>
<body>
<main class="sheet">
  <svg class="edge-band" viewBox="0 0 26 764" aria-hidden="true">
    <polygon points="0,90 26,90 26,270 0,300" fill="var(--orange)"/>
    <polygon points="0,330 26,300 26,764 0,764" fill="var(--navy)"/>
  </svg>
  <div class="faint-name" aria-hidden="true">Northpath</div>

  <div class="content">
    <header class="masthead">
      <div class="brand"><span class="dot"></span>Northpath</div>
      <div class="date">DATE <span class="fill"></span></div>
    </header>

    <section class="revision">
      <span class="section-tag">REVISION</span>
      <div class="cols">
        <div class="col">
          <div class="row"><span class="label">1.</span><span class="fill"></span></div>
          <div class="row"><span class="label">2.</span><span class="fill"></span></div>
          <div class="row"><span class="label">3.</span><span class="fill"></span></div>
          <div class="row"><span class="label">4.</span><span class="fill"></span></div>
        </div>
        <div class="col">
          <div class="row"><span class="label">5.</span><span class="fill"></span></div>
          <div class="row"><span class="label">6.</span><span class="fill"></span></div>
          <div class="row"><span class="label">7.</span><span class="fill"></span></div>
          <div class="row"><span class="label">8.</span><span class="fill"></span></div>
        </div>
      </div>
      <div class="divider"></div>
    </section>

    <section class="homework">
      <span class="section-tag">HOMEWORK</span>
      <div class="row"><span class="label">Subject:</span><span class="fill"></span></div>
      <div class="row"><span class="label">Task:</span><span class="fill"></span></div>
      <div class="row"><span class="label">Subject:</span><span class="fill"></span></div>
      <div class="row"><span class="label">Task:</span><span class="fill"></span></div>
      <div class="row"><span class="label">Subject:</span><span class="fill"></span></div>
      <div class="row"><span class="label">Task:</span><span class="fill"></span></div>
      <div class="row"><span class="label">Subject:</span><span class="fill"></span></div>
      <div class="row"><span class="label">Task:</span><span class="fill"></span></div>
      <div class="row"><span class="label">Subject:</span><span class="fill"></span></div>
      <div class="row"><span class="label">Task:</span><span class="fill"></span></div>
      <div class="divider"></div>
    </section>

    <section class="assessments">
      <span class="section-tag">ASSESSMENTS</span>
      <div class="row"><span class="label">Assessment:</span><span class="fill"></span><span class="due">Due</span><span class="fill short"></span></div>
      <div class="row"><span class="label">Element:</span><span class="fill"></span></div>
      <div class="row"><span class="label">Assessment:</span><span class="fill"></span><span class="due">Due</span><span class="fill short"></span></div>
      <div class="row"><span class="label">Element:</span><span class="fill"></span></div>
      <div class="row"><span class="label">Assessment:</span><span class="fill"></span><span class="due">Due</span><span class="fill short"></span></div>
      <div class="row"><span class="label">Element:</span><span class="fill"></span></div>
      <div class="row"><span class="label">Assessment:</span><span class="fill"></span><span class="due">Due</span><span class="fill short"></span></div>
      <div class="row"><span class="label">Element:</span><span class="fill"></span></div>
      <div class="row"><span class="label">Assessment:</span><span class="fill"></span><span class="due">Due</span><span class="fill short"></span></div>
      <div class="row"><span class="label">Element:</span><span class="fill"></span></div>
      <div class="row"><span class="label">Assessment:</span><span class="fill"></span><span class="due">Due</span><span class="fill short"></span></div>
      <div class="row"><span class="label">Element:</span><span class="fill"></span></div>
    </section>

    <section class="boxes">
      <div class="box notes">
        <h3>NOTES</h3>
        <div class="cols">
          <div class="col">
            <div class="row"><span class="label">1.</span><span class="fill"></span></div>
            <div class="row"><span class="label">2.</span><span class="fill"></span></div>
            <div class="row"><span class="label">3.</span><span class="fill"></span></div>
            <div class="row"><span class="label">4.</span><span class="fill"></span></div>
          </div>
          <div class="col">
            <div class="row"><span class="label">5.</span><span class="fill"></span></div>
            <div class="row"><span class="label">6.</span><span class="fill"></span></div>
            <div class="row"><span class="label">7.</span><span class="fill"></span></div>
            <div class="row"><span class="label">8.</span><span class="fill"></span></div>
          </div>
        </div>
      </div>
      <div class="box practice">
        <h3>PRACTICE</h3>
        <div class="row"><span class="label">1.</span><span class="fill"></span></div>
        <div class="row"><span class="label">2.</span><span class="fill"></span></div>
        <div class="row"><span class="label">3.</span><span class="fill"></span></div>
        <div class="row"><span class="label">4.</span><span class="fill"></span></div>
      </div>
    </section>

    <footer class="url">northpathstudy.com.au</footer>
  </div>
</main>
</body>
</html>
```